LINGERIE WEBSHOP - Velora casa

We are looking for design and layout design for our webshop. We are company that sells lingerie and other connected textile products liki payamas and etc..
Our website will have approx 500 different products within 2 main catogories Woman/Man) and approx. 10 subcategories
Here is what we expect form design:
-Color pallete should be black and white (if you wish you can add some accent color)
-we want to leave feeling to customers of good quality products towards to luxury
-UX should be simple. Feel free to suggest layout
-frontpage layout, product list layout, product description layout, blog layout
-responsive design, compatible with smartphone

Target Market(s)

woman buying for themself, man buying for woman

Industry/Entity Type

Lingerie

Logo Text

VELORA CASA

Number of Pages Required

4 page

Font styles to use
Sans Serif
Decorative

Requirements
Must have
• simple UX
Nice to have
• difference for sexy/luxury lingerie and daily/cozy lingerie
Should not have
• cheap feel, unreliable

```html
<!DOCTYPE html>
<html lang="en">
<head>
<meta charset="utf-8">
<title>Velora casa — Lingerie</title>
<link href="https://fonts.googleapis.com/css2?family=Playfair+Display:ital,wght@0,400;0,500;1,400&family=Mulish:wght@400;600;700&display=swap" rel="stylesheet">
<style>
:root{
  --ink:#2f2f2f;
  --text:#555;
  --muted:#777;
  --dark:#3a3a3a;
  --line:#d8d8d8;
  --hero:#e3c0b3;
  --soft:#f3f4f8;
  --icon-bg:#eceef4;
  --white:#fff;
  --serif:'Playfair Display', Georgia, serif;
  --sans:'Mulish', Arial, sans-serif;
}
*{box-sizing:border-box;margin:0;padding:0}
html,body{width:1200px;height:3916px;overflow:hidden}
body{font-family:var(--sans);color:var(--text);background:var(--white);position:relative}
.abs{position:absolute}
a{color:inherit;text-decoration:none}

/* top bar */
.topbar{top:0;left:0;width:1200px;height:41px;background:var(--dark);color:#eee;font-size:13px}
.topbar .call{left:163px;top:12px}
.topbar .social{right:160px;top:12px;display:flex;gap:14px}
.topbar .social span{width:13px;height:13px;border:1.5px solid #ddd;border-radius:2px;display:block}

/* header */
.search{left:161px;top:71px;width:180px;height:36px;border:1.5px solid #444;border-radius:18px;font-size:13px;color:#555;padding:9px 18px}
.search svg{position:absolute;right:13px;top:9px}
.wordmark{left:0;width:1200px;top:70px;text-align:center;font-family:var(--serif);font-weight:400;font-size:32px;line-height:40px;color:var(--ink)}
.tools{right:160px;top:78px;display:flex;align-items:center;gap:16px;font-size:13px;color:#444}
.tools .sep{width:1px;height:22px;background:#bbb}
.cart{position:relative}
.cart b{position:absolute;top:-6px;right:-7px;width:13px;height:13px;border-radius:50%;background:#333;color:#fff;font-size:9px;text-align:center;line-height:13px}
.nav{left:161px;top:151px;width:878px;height:51px;border-top:1px solid var(--line);display:flex;justify-content:space-between;align-items:center;padding:0 76px 0 90px;font-family:var(--serif);font-size:12.5px;color:#555;letter-spacing:.3px}
.nav .active{color:var(--ink);font-weight:500;border-bottom:1px solid var(--ink)}
.nav .div{width:1px;height:11px;background:#ccc}

/* hero */
.hero{top:202px;left:0;width:1200px;height:464px;background:linear-gradient(90deg,#dcb3a5 0%,var(--hero) 40%,#e6c6ba 100%)}
.hero .photo{left:140px;top:0;width:520px;height:464px;background:radial-gradient(ellipse at 55% 45%,#c99b87 0%,#d5ad9e 45%,rgba(227,192,179,0) 75%)}
.hero .kicker{left:727px;top:118px;font-size:14px;letter-spacing:2px;color:#444}
.hero h1{left:727px;top:140px;font-family:var(--serif);font-weight:400;font-size:55px;line-height:59px;color:#222}
.hero p{left:727px;top:274px;font-size:14px;color:#444}
.btn-outline{border:1.5px solid #444;border-radius:20px;font-family:var(--serif);font-size:13px;color:#333;display:flex;align-items:center;justify-content:center;letter-spacing:.3px}
.hero .btn-outline{left:724px;top:309px;width:120px;height:37px}
.dots{display:flex;gap:10px}
.dots i{width:11px;height:11px;border-radius:50%;border:1.5px solid #666;background:#fff;display:block}
.dots i.on{background:#666}
.hero .dots{left:574px;top:430px}

/* features */
.feature{top:745px;width:225px;text-align:center}
.feature .ic{width:58px;height:58px;border-radius:50%;background:var(--icon-bg);margin:0 auto;display:flex;align-items:center;justify-content:center}
.feature h3{font-family:var(--serif);font-weight:400;font-size:17px;color:#333;margin-top:16px;letter-spacing:.4px}
.feature p{font-size:12px;line-height:19px;margin-top:10px;color:#555}

/* section headings */
.kick{left:0;width:1200px;text-align:center;font-size:13.5px;letter-spacing:2px;color:#444}
.title{left:0;width:1200px;text-align:center;font-family:var(--serif);font-weight:400;font-size:40px;color:#333;letter-spacing:.5px}
.rule{left:540px;width:120px;height:1.5px;background:#444}

/* products */
.product{top:1083px;width:202px;text-align:center}
.product .img{width:202px;height:207px;background:linear-gradient(#ece9e6,#d9d4d0)}
.product h4{font-family:var(--serif);font-weight:400;font-size:14.5px;color:#444;margin-top:16px}
.product .price{font-family:var(--serif);font-size:14.5px;color:#444;margin-top:11px}
.product .btn-outline{width:120px;height:30px;margin:15px auto 0;font-size:12px}
.product .btn-outline.solid{background:#333;color:#fff;border-color:#333}
.arrow{top:1226px;width:29px;height:29px;border-radius:50%;border:1.5px solid #bbb;display:flex;align-items:center;justify-content:center}
.arrow.next{border-color:#222}

/* promo */
.promo{top:1474px;width:429px;height:299px;background:linear-gradient(100deg,#e3ddd8,#f4f1ee)}
.promo h3{position:absolute;font-family:var(--serif);font-weight:400;font-size:31px;line-height:31px;color:#333}
.promo p{position:absolute;font-family:var(--serif);font-style:italic;font-size:15px;line-height:18px;color:#333}

/* testimonials */
.testi{top:1848px;left:0;width:1200px;height:434px;background:linear-gradient(100deg,#f2ece8,#f7f2ef 50%,#eee9e5)}
.testi .q{left:0;width:1200px;top:188px;text-align:center;font-family:var(--serif);font-size:16px;line-height:29px;color:#333}
.testi .who{left:0;width:1200px;top:272px;text-align:center;font-family:var(--serif);font-size:15px;color:#333}
.testi .role{left:0;width:1200px;top:294px;text-align:center;font-family:var(--serif);font-style:italic;font-size:13px;color:#444}
.testi .dots{left:574px;top:364px}

/* brands */
.brands{top:2372px;left:200px;width:800px;display:flex;justify-content:space-between;align-items:center;font-family:var(--serif);font-size:17px;color:#555}
.brands span{display:flex;align-items:center;gap:7px}
.brands i{width:10px;height:10px;border-radius:50%;background:#bbb;display:block}

/* blog */
.blog{top:2510px;left:0;width:1200px;height:597px;background:var(--soft)}
.post{top:2675px;width:278px}
.post .img{height:180px}
.post .date{font-size:13px;color:#444;margin-top:17px;display:flex;align-items:center;gap:6px;padding-left:2px}
.post p{font-size:13px;line-height:24.5px;color:#333;font-weight:700;margin-top:6px;padding-left:2px}
.btn-dark{background:#3a3a3a;color:#fff;border-radius:20px;font-family:var(--serif);display:flex;align-items:center;justify-content:center;letter-spacing:.3px}

/* newsletter */
.news h2{left:0;width:1200px;top:3180px;text-align:center;font-family:var(--serif);font-weight:400;font-size:38px;line-height:45px;color:#333}
.news p{left:0;width:1200px;top:3285px;text-align:center;font-size:13px;color:#444}
.news .field{left:412px;top:3343px;width:375px;height:40px;border:1.5px solid #444;border-radius:20px;font-size:12px;color:#444;display:flex;align-items:center;justify-content:center}

/* footer */
.footer{top:3514px;left:0;width:1200px;height:402px;background:#3b3b3b;color:#ddd}
.fcol{top:83px}
.fcol h5{font-family:var(--serif);font-weight:400;font-size:15px;color:#eee;letter-spacing:.3px}
.fcol ul{list-style:none;margin-top:12px}
.fcol li{font-size:13px;line-height:28.5px;color:#ddd}
.fcol li::before{content:"›";margin-right:10px}
.fdiv{top:77px;width:1px;height:200px;background:#555}
.fsocial{display:flex;gap:8px;margin-top:16px}
.fsocial span{width:22px;height:22px;background:#666;display:block}
.fwordmark{margin-top:26px;font-family:var(--serif);font-weight:400;font-size:24px;line-height:30px;color:#eee}
.fline{left:161px;top:345px;width:878px;height:1px;background:#555}
.copy{left:163px;top:368px;font-size:12px;color:#ddd}
.pay{right:162px;top:365px;display:flex;align-items:center;gap:5px;font-size:12px;color:#ddd}
.pay span{width:29px;height:18px;border-radius:2px;background:#e8e8e8;display:block}
.pay b{font-weight:400;margin-right:6px}
</style>
</head>
<body>

<!-- top bar -->
<div class="abs topbar">
  <div class="abs call">Call Us Now: 555 014 2290</div>
  <div class="abs social"><span></span><span></span><span></span><span></span></div>
</div>

<!-- header -->
<div class="abs search">Search here
  <svg width="16" height="16" viewBox="0 0 16 16" fill="none" stroke="#333" stroke-width="2"><circle cx="6.5" cy="6.5" r="5"/><path d="M10.5 10.5l4 4"/></svg>
</div>
<div class="abs wordmark">Velora Casa</div>
<div class="abs tools">
  <span>USD ▾</span>
  <span class="cart"><svg width="22" height="20" viewBox="0 0 22 20" fill="none" stroke="#333" stroke-width="1.8"><path d="M1 2h3l3 11h11l2-8H6"/><circle cx="9" cy="17" r="1.5" fill="#333"/><circle cx="16" cy="17" r="1.5" fill="#333"/></svg><b>0</b></span>
  <span class="sep"></span>
  <svg width="22" height="22" viewBox="0 0 22 22" fill="none" stroke="#333" stroke-width="1.8"><circle cx="11" cy="11" r="9.5"/><circle cx="11" cy="9" r="3.5"/><path d="M4.5 17.5c2-3 11-3 13 0"/></svg>
</div>
<nav class="abs nav">
  <a class="active">HOME</a><span class="div"></span>
  <a>BRAS</a><span class="div"></span>
  <a>PANTIES</a><span class="div"></span>
  <a>CLEARANCE!</a><span class="div"></span>
  <a>BLOG</a><span class="div"></span>
  <a>ABOUT ▾</a>
</nav>

<!-- hero -->
<section class="abs hero">
  <div class="abs photo" role="img" aria-label="Model wearing a dark plunge bra against a blush backdrop"></div>
  <div class="abs kicker">LOOK YOUR BEST</div>
  <h1 class="abs">Personalized<br>Bra Fittings</h1>
  <p class="abs">Find something special for women of all sizes.</p>
  <a class="abs btn-outline">BUY NOW</a>
  <div class="abs dots"><i></i><i class="on"></i><i></i></div>
</section>

<!-- features -->
<div class="abs feature" style="left:150px">
  <div class="ic"><svg width="30" height="30" viewBox="0 0 30 30" fill="none" stroke="#444" stroke-width="1.4"><circle cx="16" cy="11" r="7"/><path d="M16 7v8M18 8.5h-3a1.5 1.5 0 000 3h2a1.5 1.5 0 010 3h-3"/><path d="M3 20h5l5 3h7l4-4"/></svg></div>
  <h3>100% MONEY BACK</h3><p>We offer 100% money-back<br>guarantee within 60 days.</p>
</div>
<div class="abs feature" style="left:375px">
  <div class="ic"><svg width="30" height="30" viewBox="0 0 30 30" fill="none" stroke="#444" stroke-width="1.4"><path d="M5 4h4l3 16h12"/><rect x="12" y="8" width="11" height="9"/><circle cx="13" cy="24" r="2"/><circle cx="22" cy="24" r="2"/></svg></div>
  <h3>FREE SHIPPING</h3><p>We provide you with fast and free<br>delivery on orders of $200+</p>
</div>
<div class="abs feature" style="left:600px">
  <div class="ic"><svg width="30" height="30" viewBox="0 0 30 30" fill="none" stroke="#444" stroke-width="1.5"><circle cx="15" cy="15" r="12"/><path d="M10 20l10-10"/><circle cx="10.5" cy="10.5" r="2"/><circle cx="19.5" cy="19.5" r="2"/></svg></div>
  <h3>MEMBER DISCOUNT</h3><p>Enjoy significant exclusive savings on<br>our store products and services</p>
</div>
<div class="abs feature" style="left:825px">
  <div class="ic"><svg width="30" height="30" viewBox="0 0 30 30" fill="none" stroke="#444" stroke-width="1.5"><path d="M6 17v-3a9 9 0 0118 0v3"/><rect x="4" y="16" width="5" height="8" rx="2"/><rect x="21" y="16" width="5" height="8" rx="2"/><path d="M23 24c0 3-4 4-7 4"/></svg></div>
  <h3>24/7 ONLINE SUPPORT</h3><p>Get immediate help, ongoing<br>support &amp; information any time</p>
</div>

<!-- featured products -->
<div class="abs kick" style="top:965px">TREDING PRODUCTS OF HIGH FASHION</div>
<h2 class="abs title" style="top:985px">FEATURED PRODUCTS</h2>
<div class="abs rule" style="top:1044px"></div>

<div class="abs arrow" style="left:92px"><svg width="12" height="12" viewBox="0 0 12 12" fill="none" stroke="#bbb" stroke-width="1.5"><path d="M11 6H1M5 2L1 6l4 4"/></svg></div>
<div class="abs arrow next" style="left:1078px"><svg width="12" height="12" viewBox="0 0 12 12" fill="none" stroke="#222" stroke-width="1.5"><path d="M1 6h10M7 2l4 4-4 4"/></svg></div>

<div class="abs product" style="left:161px">
  <div class="img" role="img" aria-label="Nude lace bodysuit on a model" style="background:linear-gradient(#e4ddd6,#cbb9a9)"></div>
  <h4>Bralette Serafina</h4><div class="price">$80.00</div><a class="btn-outline solid">ADD TO CART</a>
</div>
<div class="abs product" style="left:386px">
  <div class="img" role="img" aria-label="Floral print bustier chemise on a model" style="background:linear-gradient(#eae8e6,#bdbab6)"></div>
  <h4>Livia Underwired Bustier</h4><div class="price">$39.00</div><a class="btn-outline">ADD TO CART</a>
</div>
<div class="abs product" style="left:611px">
  <div class="img" role="img" aria-label="Printed two-piece set with coral briefs on a model" style="background:linear-gradient(#ebe7e3,#d8c1b3)"></div>
  <h4>Amara Lisle Coast Two</h4><div class="price">$49.00</div><a class="btn-outline">ADD TO CART</a>
</div>
<div class="abs product" style="left:836px">
  <div class="img" role="img" aria-label="Black lace corset bodysuit on a model" style="background:linear-gradient(#ecebea,#8e8b89)"></div>
  <h4>Bodysuit Noctura</h4><div class="price">$43.00</div><a class="btn-outline">ADD TO CART</a>
</div>

<!-- promo banners -->
<div class="abs promo" style="left:161px" role="img" aria-label="Model in white lingerie seated by a bright window">
  <h3 style="left:221px;top:94px">New Classic<br>Models</h3>
  <p style="left:221px;top:167px">Stay elegant, look and<br>feel new.</p>
</div>
<div class="abs promo" style="left:610px;background:linear-gradient(100deg,#d9d2cd,#eef0f2)" role="img" aria-label="Model in a white bra wrapped in a grey throw">
  <h3 style="left:240px;top:94px">New Arrivals<br>Sexy Sets</h3>
  <p style="left:240px;top:167px">Exclusive items for<br>your naughty nights.</p>
</div>

<!-- testimonials -->
<section class="abs testi" role="img" aria-label="Faded image of a model reclining in lingerie">
  <div class="abs kick" style="top:74px">WHAT PEOPLE SAY ABOUT US</div>
  <h2 class="abs title" style="top:96px">TESTIMONIALS</h2>
  <p class="abs q">" I was surprised with such an excellent quality... I would definitely use this site again and again and<br>recommend it to others. "</p>
  <div class="abs who">DANA WHITMORE</div>
  <div class="abs role">Lorem Ipsum</div>
  <div class="abs dots"><i></i><i class="on"></i><i></i></div>
</section>

<!-- brands -->
<div class="abs brands">
  <span><i></i>Solenne</span>
  <span><i></i>Belmira</span>
  <span><i></i>Aurelle</span>
  <span><i></i>Mira Mira</span>
  <span><i></i>Velvet Lane</span>
  <span><i></i>Petal Notes</span>
</div>

<!-- blog -->
<section class="abs blog"></section>
<h2 class="abs title" style="top:2580px">LATEST BLOG POSTS</h2>
<div class="abs rule" style="top:2636px"></div>

<article class="abs post" style="left:161px">
  <div class="img" role="img" aria-label="Model holding a bouquet of lilac flowers" style="background:linear-gradient(135deg,#4e4a52,#b9a7b3 60%,#e6e0e4)"></div>
  <div class="date"><svg width="12" height="12" viewBox="0 0 12 12" fill="none" stroke="#444" stroke-width="1.2"><rect x="1" y="2" width="10" height="9"/><path d="M1 5h10M3.5 1v2M8.5 1v2"/></svg>20 Jul 2020</div>
  <p>Praesent scelerisque dolor vitae dignissim sodales duis laoreet tellus ultricies dictum pharetra praesent euismod</p>
</article>
<article class="abs post" style="left:461px">
  <div class="img" role="img" aria-label="Stack of pink, black and floral bras" style="background:linear-gradient(135deg,#d9a9ad,#3a3438 55%,#c9b9c8)"></div>
  <div class="date"><svg width="12" height="12" viewBox="0 0 12 12" fill="none" stroke="#444" stroke-width="1.2"><rect x="1" y="2" width="10" height="9"/><path d="M1 5h10M3.5 1v2M8.5 1v2"/></svg>20 Jul 2020</div>
  <p>Nullam accumsan, quam a auctor laoreeti, urna ipsum imperdiet neque, at consectiet enim sem ac nisl.</p>
</article>
<article class="abs post" style="left:761px">
  <div class="img" role="img" aria-label="Model in cream lace lingerie lying on a bed" style="background:linear-gradient(135deg,#f1e4dc,#d8b8a6 60%,#8a6a5c)"></div>
  <div class="date"><svg width="12" height="12" viewBox="0 0 12 12" fill="none" stroke="#444" stroke-width="1.2"><rect x="1" y="2" width="10" height="9"/><path d="M1 5h10M3.5 1v2M8.5 1v2"/></svg>20 Jul 2020</div>
  <p>Fusce sed laoreet odio. Fusce rutrum rutru posuere pellentesque et congue urna, vele dapibus felis proin consectetur.</p>
</article>
<a class="abs btn-dark" style="left:540px;top:3001px;width:120px;height:31px;font-size:12px">VIEW ALL</a>

<!-- newsletter -->
<section class="news">
  <h2 class="abs">GET THE LATEST NEWS<br>DELIVERED DAILY!</h2>
  <p class="abs">Sign up for our newsletter to recive the latest news, exlusive offers, and other discount information.</p>
  <div class="abs field">Enter your email</div>
  <a class="abs btn-dark" style="left:525px;top:3395px;width:150px;height:40px;font-size:15px">SUBSCRIBE</a>
</section>

<!-- footer -->
<footer class="abs footer">
  <div class="abs fcol" style="left:163px"><h5>QUICK LINKS</h5><ul><li>Home</li><li>Search</li><li>Clearance!</li><li>Blog</li><li>About Us</li><li>Contact Us</li></ul></div>
  <div class="abs fdiv" style="left:330px"></div>
  <div class="abs fcol" style="left:394px"><h5>COLLECTIONS</h5><ul><li>Accessories</li><li>Bras</li><li>Collection</li><li>Combinations</li><li>Panties</li><li>Sexy Lingerie</li></ul></div>
  <div class="abs fdiv" style="left:572px"></div>
  <div class="abs fcol" style="left:636px"><h5>MY ACCOUNT</h5><ul><li>My Account</li><li>My Addresses</li><li>My Cart</li></ul></div>
  <div class="abs fdiv" style="left:808px"></div>
  <div class="abs fcol" style="left:870px"><h5>FOLLOW US ON</h5>
    <div class="fsocial"><span></span><span></span><span></span><span></span></div>
    <div class="fwordmark">Velora Casa</div>
  </div>
  <div class="abs fline"></div>
  <div class="abs copy">Copyright © 2020 VELORA CASA. All Rights Reserved.</div>
  <div class="abs pay"><b>We Accept :</b><span></span><span></span><span></span><span></span><span></span></div>
</footer>

</body>
</html>
```